New Venture ----Alloy wheel refurbishment/ Wheel Repair Solutions .Needs a design logo

Paltrey Auto Body Repairs
Corranmore East ,
Newmarket Co.Cork. K73 WM58 NTR APPROVED 0869415837 02918356 pmpanelworks@fernmail.example
need business cards to advertise the' Brontel Vertical Alloy Wheel Lathe 'machine we have just purchased .

```html
<!DOCTYPE html>
<html lang="en">
<head>
<meta charset="utf-8">
<title>Paltrey Auto Body Repairs – Business Card</title>
<link rel="stylesheet" href="https://fonts.googleapis.com/css2?family=Roboto:wght@400;500;700&display=swap">
<style>
  :root {
    --backdrop: #2c2c2c;
    --brand-red: #e0141b;
    --ink: #151515;
    --paper: #f2f2f2;
    --paper-shade: #dcdcdc;
    --white: #f5f5f5;
    --wheel-dark: #1d1d1d;
    --wheel-mid: #4a4a4a;
  }
  html, body {
    margin: 0;
    padding: 0;
    width: 1200px;
    height: 1138px;
    overflow: hidden;
    background: var(--backdrop);
    font-family: "Roboto", Arial, sans-serif;
  }
  .canvas {
    position: relative;
    width: 1200px;
    height: 1138px;
  }
  .card {
    position: absolute;
    width: 620px;
    height: 375px;
    border-radius: 13px;
    overflow: hidden;
  }
  /* ---------- Front ---------- */
  .card--front {
    left: 274px;
    top: 186px;
  }
  .card__photo {
    position: absolute;
    inset: 0;
    background:
      radial-gradient(circle at 50% 45%, var(--wheel-mid) 0%, #333 30%, #262626 48%, var(--wheel-dark) 70%, #121212 100%);
  }
  .card__photo::after {
    content: "";
    position: absolute;
    inset: 0;
    background: rgba(0, 0, 0, 0.35);
  }
  .front__content {
    position: absolute;
    inset: 0;
    text-align: center;
    color: var(--white);
  }
  .brand-name {
    margin: 0;
    font-weight: 700;
    text-transform: uppercase;
    letter-spacing: 1px;
    line-height: 1.05;
  }
  .front__name {
    position: absolute;
    left: 0;
    right: 0;
    top: 94px;
    font-size: 42px;
    color: var(--white);
  }
  .front__address {
    position: absolute;
    left: 0;
    right: 0;
    top: 250px;
    font-size: 16px;
    margin: 0;
  }
  .front__approval {
    position: absolute;
    left: 0;
    right: 0;
    top: 299px;
    font-size: 16px;
    font-weight: 500;
    color: var(--brand-red);
    margin: 0;
  }
  /* ---------- Back ---------- */
  .card--back {
    left: 276px;
    top: 608px;
    background: linear-gradient(180deg, #f6f6f6 0%, var(--paper) 55%, #e6e6e6 100%);
  }
  .back__photo {
    position: absolute;
    right: 0;
    top: 0;
    width: 240px;
    height: 375px;
    background: linear-gradient(110deg, rgba(220,220,220,0) 0%, rgba(205,205,205,0.55) 45%, rgba(190,190,190,0.7) 75%, rgba(215,215,215,0.4) 100%);
  }
  .back__name {
    position: absolute;
    left: 34px;
    top: 40px;
    font-size: 32px;
    color: var(--ink);
  }
  .contact {
    position: absolute;
    left: 34px;
    top: 250px;
    margin: 0;
    padding: 0;
    list-style: none;
    font-size: 17px;
    color: var(--ink);
  }
  .contact__item {
    display: flex;
    align-items: center;
    height: 28px;
  }
  .contact__icon {
    width: 16px;
    height: 14px;
    margin-right: 17px;
    flex: none;
  }
  .contact__address {
    margin-top: 7px;
  }
  .approval-badge {
    position: absolute;
    left: 418px;
    top: 288px;
    width: 148px;
    height: 50px;
    text-align: center;
  }
  .approval-badge svg {
    position: absolute;
    inset: 0;
  }
  .approval-badge__code {
    position: relative;
    display: block;
    padding-top: 8px;
    font-size: 17px;
    font-weight: 500;
    color: var(--ink);
  }
  .approval-badge__label {
    position: relative;
    display: block;
    margin-top: 6px;
    font-size: 17px;
    font-weight: 500;
    color: var(--brand-red);
  }
</style>
</head>
<body>
<div class="canvas">

  <section class="card card--front">
    <div class="card__photo" role="img" aria-label="Close-up photograph of a dark alloy car wheel with split spokes"></div>
    <div class="front__content">
      <h1 class="brand-name front__name">Paltrey Auto<br>Body Repairs</h1>
      <p class="front__address">Corranmore East, Newmarket Co. Cork.</p>
      <p class="front__approval">K73 WM58 NTR APPROVED</p>
    </div>
  </section>

  <section class="card card--back">
    <div class="back__photo" role="img" aria-label="Faint photograph of alloy wheel spokes"></div>
    <h2 class="brand-name back__name">Paltrey Auto<br>Body Repairs</h2>

    <ul class="contact">
      <li class="contact__item">
        <svg class="contact__icon" viewBox="0 0 16 14" aria-hidden="true">
          <path d="M1 4 Q8 -1 15 4 L13 6 L11 4.5 L5 4.5 L3 6 Z" fill="var(--brand-red)"/>
          <path d="M4 7 L12 7 L14 13 L2 13 Z" fill="var(--brand-red)"/>
          <circle cx="8" cy="10" r="1.6" fill="#fff"/>
        </svg>
        0869415837, 02918356
      </li>
      <li class="contact__item">
        <svg class="contact__icon" viewBox="0 0 16 14" aria-hidden="true">
          <rect x="1" y="2" width="14" height="10" fill="var(--brand-red)"/>
          <path d="M1 2 L8 8 L15 2" fill="none" stroke="#fff" stroke-width="1.3"/>
        </svg>
        pmpanelworks@fernmail.example
      </li>
      <li class="contact__item contact__address">Corranmore East, Newmarket Co. Cork.</li>
    </ul>

    <div class="approval-badge">
      <svg width="148" height="50" viewBox="0 0 148 50" aria-hidden="true">
        <path d="M28 42 L6 42 Q1 42 1 37 L1 6 Q1 1 6 1 L142 1 Q147 1 147 6 L147 37 Q147 42 142 42 L120 42"
              fill="none" stroke="var(--brand-red)" stroke-width="1.6"/>
      </svg>
      <span class="approval-badge__code">K73 WM58 NTR</span>
      <span class="approval-badge__label">APPROVED</span>
    </div>
  </section>

</div>
</body>
</html>
```